Salon website

Need a web design for a new blow dry and hair extension boutique in CT
would like the color scheme to be gray, white and tiffany blue
Create a web site with about 4 pages showing
1 about us page
1 blow dry services page
1 hair extension services page
1 contact us page
1 membership page
1 parties page

Industry/Entity Type

Boutique

Colors
86cfc6
cfeae6
33b7a4
aaaaaa
cbcbcb
ffffff

```html
<!DOCTYPE html>
<html lang="en">
<head>
<meta charset="UTF-8">
<title>Memberships – Velour Boutique</title>
<link rel="stylesheet" href="https://fonts.googleapis.com/css2?family=Jost:wght@300;400&display=swap">
<style>
  :root {
    --aqua: #81d8d0;
    --gray-band: #cbcbcb;
    --white: #ffffff;
    --ink: #5a5a5a;
    --photo-light: #d9d9d9;
    --photo-dark: #6e6e6e;
  }
  * { margin: 0; padding: 0; box-sizing: border-box; }
  html, body { width: 1200px; height: 825px; overflow: hidden; background: var(--white); }
  body { position: relative; font-family: "Jost", sans-serif; color: var(--white); }

  .brand {
    position: absolute; left: 0; top: 0; width: 179px; height: 114px;
    background: var(--aqua);
    display: flex; flex-direction: column; align-items: center; justify-content: center; gap: 6px;
  }
  .brand-mark { width: 56px; height: 56px; border-radius: 50%; background: var(--ink); opacity: .85; }
  .brand-name { font-weight: 300; font-size: 17px; letter-spacing: 4px; color: var(--ink); }

  .main-nav {
    position: absolute; left: 195px; top: 0; width: 1005px; height: 114px;
    background: var(--aqua);
  }
  .main-nav a {
    position: absolute; top: 0; height: 114px; line-height: 106px;
    font-weight: 300; font-size: 21px; letter-spacing: .5px;
    color: var(--white); text-decoration: none; text-align: center; white-space: nowrap;
  }
  .main-nav a.is-current { background: var(--white); color: var(--ink); }

  .content-band {
    position: absolute; left: 0; top: 154px; width: 1200px; height: 486px;
    background: var(--gray-band);
  }
  .page-title { position: absolute; left: 16px; top: 19px; font-weight: 300; font-size: 28px; letter-spacing: .5px; }
  .levels { position: absolute; left: 76px; top: 73px; width: 840px; }
  .level { margin-bottom: 24.7px; }
  .level h2 { font-weight: 300; font-size: 19px; line-height: 24.7px; }
  .level p { font-weight: 300; font-size: 18.5px; line-height: 24.7px; white-space: nowrap; }
  .level p .indent { display: inline-block; width: 30px; }

  .salon-photo {
    position: absolute; left: 932px; top: 47px; width: 248px; height: 409px;
    background: var(--white); padding: 8px;
  }
  .salon-photo svg { display: block; width: 234px; height: 395px; }

  .site-footer {
    position: absolute; left: 0; top: 688px; width: 1200px; height: 137px;
    background: var(--aqua);
  }
  .site-footer span { position: absolute; top: 71px; font-weight: 300; font-size: 21px; letter-spacing: .5px; white-space: nowrap; }
</style>
</head>
<body>
  <header>
    <div class="brand">
      <div class="brand-mark"></div>
      <div class="brand-name">VELOUR</div>
    </div>
    <nav class="main-nav">
      <a href="#" style="left:0;width:160px">ABOUT US</a>
      <a href="#" style="left:160px;width:130px">BLOW DRY</a>
      <a href="#" style="left:290px;width:232px">HAIR EXTENSIONS</a>
      <a href="#" style="left:522px;width:150px">CONTACT US</a>
      <a href="#" class="is-current" style="left:691px;width:176px">MEMBERSHIPS</a>
      <a href="#" style="left:867px;width:138px">PARTIES</a>
    </nav>
  </header>

  <main class="content-band">
    <h1 class="page-title">MEMBERSHIPS</h1>
    <div class="levels">
      <section class="level">
        <h2>LEVEL 1</h2>
        <p><span class="indent"></span>Donec nisl nisi, facilisis eu tortor blandit, commodo laoreet mi. Integer vulputate<br>non orci non aliquam. Maecenas volutpat ante id venenatis auctor. Nam dignissim blan-<br>dit diam at volutpat. Suspendisse tempor nec arcu tempus cursus. Maecenas lobortis a<br>mi sed faucibus.</p>
      </section>
      <section class="level">
        <h2>LEVEL 2</h2>
        <p><span class="indent"></span>Vivamus fringilla mauris in porta tempus. Aenean condimentum, lectus ut vulputate<br>tempus, tortor turpis placerat neque, sit amet consectetur quam tortor pharetra enim.<br>Ut faucibus orci non hendrerit vulputate. Nam gravida euismod ipsum, quis convallis<br>massa molestie vel.</p>
      </section>
      <section class="level">
        <h2>LEVEL 3</h2>
        <p><span class="indent"></span>Sed aliquet quam vel fermentum scelerisque. Cras id placerat dolor. Integer quis<br>euismod turpis.</p>
      </section>
    </div>
    <figure class="salon-photo">
      <svg role="img" aria-label="Black and white photo of the salon interior with styling chairs and round mirrors" viewBox="0 0 234 395">
        <defs>
          <linearGradient id="salonTone" x1="0" y1="0" x2="0" y2="1">
            <stop offset="0" stop-color="#6e6e6e"/>
            <stop offset=".55" stop-color="#d9d9d9"/>
            <stop offset="1" stop-color="#f2f2f2"/>
          </linearGradient>
        </defs>
        <rect width="234" height="395" fill="url(#salonTone)"/>
      </svg>
    </figure>
  </main>

  <footer class="site-footer">
    <span style="left:376px">© 2014 VELOUR BOUTIQUE</span>
    <span style="left:672px">PRIVACY POLICY</span>
  </footer>
</body>
</html>
```